Design for a 4 screens mobile app: Brightnook

The app is a compact but illustrated phone/address book...
We need a design for the 5 screens of the app (see screens attached):
a) "index" : 1 screen with 6 pictures of contact person
b) "contact list" : 1 screen, to manage (add/del/edit) the contacts of the phone/address book
c) "add contact" : 1 screen to add a contact (a picture + a phone number)
d) "update contact" : similar to "add"
e) "fields missing" : add/edit screens in "error" state
We also need the ico design + loading screen.
No specific guidelines, nor logo or whatever.
It will be a free app distributed on iOS and Androïd.
We just want to make it looking nice & very usable for end users.
B2C

```html
<!DOCTYPE html>
<html lang="en">
<head>
<meta charset="utf-8">
<title>Brightnook – Index</title>
<link rel="stylesheet" href="https://fonts.googleapis.com/css2?family=Raleway:wght@400;500&family=Lato:wght@400&display=swap">
<style>
  :root {
    --header-dark: #8ba1b3;
    --header-light: #96acbd;
    --ink-light: #ffffff;
    --number: #9eb0c0;
    --divider: #eceff2;
    --surface: #ffffff;
    --delete: #f89292;
    --tab-main: #86a2b7;
    --tab-side: #9db3c5;
  }
  * { box-sizing: border-box; margin: 0; padding: 0; }
  html, body { width: 747px; height: 1200px; overflow: hidden; background: var(--surface); }
  .app { width: 747px; height: 1200px; display: flex; flex-direction: column; font-family: "Raleway", sans-serif; }

  .app-header {
    height: 140px; position: relative; color: var(--ink-light);
    background: linear-gradient(112deg, var(--header-light) 0%, var(--header-light) 58%, var(--header-dark) 58%, var(--header-dark) 100%);
  }
  .status-bar {
    height: 46px; display: flex; align-items: center; justify-content: space-between;
    padding: 0 22px 0 22px; font-family: "Lato", sans-serif; font-size: 20px;
  }
  .status-left, .status-right { display: flex; align-items: center; gap: 8px; width: 220px; }
  .status-right { justify-content: flex-end; }
  .status-time { font-weight: 400; }
  .nav-bar { position: absolute; left: 0; right: 0; top: 46px; height: 94px; display: flex; align-items: center; justify-content: center; }
  .nav-title { font-size: 33px; font-weight: 400; letter-spacing: 0.5px; }
  .nav-back { position: absolute; left: 52px; top: 32px; }
  .nav-add { position: absolute; right: 46px; top: 32px; }

  .contact-list { flex: 1; list-style: none; padding-top: 24px; }
  .contact-row { height: 158px; position: relative; display: flex; align-items: center; }
  .contact-row::after {
    content: ""; position: absolute; left: 29px; width: 695px; bottom: 0; height: 2px; background: var(--divider);
  }
  .contact-row:last-child::after { display: none; }
  .contact-photo { width: 180px; height: 140px; margin-left: 29px; margin-top: -6px; flex: none; }
  .contact-number {
    position: absolute; left: 209px; width: 370px; text-align: center;
    font-size: 22px; color: var(--number); letter-spacing: 0.4px; margin-top: -6px;
  }
  .row-delete {
    position: absolute; left: 618px; right: 0; top: 0; bottom: 0; background: var(--delete);
    display: flex; align-items: center; justify-content: center;
  }

  .tab-bar { height: 84px; display: flex; }
  .tab-settings { width: 598px; background: var(--tab-main); display: flex; align-items: center; justify-content: center; }
  .tab-more { flex: 1; background: var(--tab-side); display: flex; align-items: center; justify-content: center; gap: 8px; }
  .tab-more span { width: 10px; height: 10px; border-radius: 50%; background: #7f9bb0; }
</style>
</head>
<body>
<div class="app">
  <header class="app-header">
    <div class="status-bar">
      <div class="status-left">
        <svg width="66" height="12" viewBox="0 0 66 12" aria-hidden="true">
          <circle cx="6" cy="6" r="5" fill="#fff"/><circle cx="19" cy="6" r="5" fill="#fff"/><circle cx="32" cy="6" r="5" fill="#fff"/>
          <circle cx="45" cy="6" r="4.3" fill="none" stroke="#fff" stroke-width="1.2"/><circle cx="58" cy="6" r="4.3" fill="none" stroke="#fff" stroke-width="1.2"/>
        </svg>
        <span class="carrier">CELLA</span>
        <svg width="22" height="16" viewBox="0 0 22 16" aria-hidden="true" fill="none" stroke="#fff" stroke-width="2" stroke-linecap="round">
          <path d="M2 6a13 13 0 0 1 18 0"/><path d="M5.5 9.5a8 8 0 0 1 11 0"/><circle cx="11" cy="13.5" r="1.3" fill="#fff" stroke="none"/>
        </svg>
      </div>
      <span class="status-time">4:21 PM</span>
      <div class="status-right">
        <svg width="12" height="20" viewBox="0 0 12 20" aria-hidden="true" fill="none" stroke="#dfe6ec" stroke-width="1.6">
          <path d="M1 5l10 9-5 4V2l5 4-10 9"/>
        </svg>
        <span>100%</span>
        <svg width="44" height="18" viewBox="0 0 44 18" aria-hidden="true">
          <rect x="1" y="1" width="38" height="16" rx="3" fill="none" stroke="#fff" stroke-width="1.5"/>
          <rect x="3" y="3" width="34" height="12" rx="1.5" fill="#fff"/>
          <rect x="40.5" y="6" width="2.5" height="6" rx="1" fill="#fff"/>
        </svg>
      </div>
    </div>
    <div class="nav-bar">
      <svg class="nav-back" width="20" height="32" viewBox="0 0 20 32" aria-label="Back" role="img">
        <path d="M17 2L3 16l14 14" fill="none" stroke="#fff" stroke-width="2.4" stroke-linecap="round" stroke-linejoin="round"/>
      </svg>
      <h1 class="nav-title">Index</h1>
      <svg class="nav-add" width="32" height="32" viewBox="0 0 32 32" aria-label="Add contact" role="img">
        <path d="M16 1v30M1 16h30" stroke="#fff" stroke-width="2.6" stroke-linecap="round"/>
      </svg>
    </div>
  </header>

  <ul class="contact-list">
    <li class="contact-row">
      <div class="contact-photo" role="img" aria-label="Contact photo: smiling woman in a cap outdoors" style="background:linear-gradient(135deg,#9aa58a,#d8b99a 50%,#6f7460)"></div>
      <span class="contact-number">2857413096</span>
    </li>
    <li class="contact-row">
      <div class="contact-photo" role="img" aria-label="Contact photo: woman with silver hair and sunglasses" style="background:linear-gradient(160deg,#c9cfd3,#ece8e4 55%,#e0573a)"></div>
      <span class="contact-number">9370518264</span>
    </li>
    <li class="contact-row">
      <div class="contact-photo" role="img" aria-label="Contact photo: red-haired woman smiling" style="background:linear-gradient(110deg,#e9d3c2,#c9805a 55%,#eef0f1)"></div>
      <span class="contact-number">1204875632</span>
    </li>
    <li class="contact-row">
      <div class="contact-photo" role="img" aria-label="Contact photo: bearded man with glasses" style="background:linear-gradient(135deg,#8f8a7a,#b89079 50%,#4c4136)"></div>
      <span class="contact-number">814702355</span>
    </li>
    <li class="contact-row">
      <div class="contact-photo" role="img" aria-label="Contact photo: young woman with long red hair" style="background:linear-gradient(120deg,#b7b4ae,#c77a4c 50%,#e7e4e0)"></div>
      <span class="contact-number">762519048</span>
      <div class="row-delete">
        <svg width="32" height="40" viewBox="0 0 32 40" aria-label="Delete contact" role="img" fill="none" stroke="#fff" stroke-width="1.8" stroke-linecap="round" stroke-linejoin="round">
          <path d="M2 7h28M11 7V3h10v4M5 7l2 31h18l2-31M11 12v21M16 12v21M21 12v21"/>
        </svg>
      </div>
    </li>
    <li class="contact-row">
      <div class="contact-photo" role="img" aria-label="Contact photo: woman with curly hair and green scarf" style="background:linear-gradient(150deg,#c7cdd0,#6a4a36 50%,#2f9a7c)"></div>
      <span class="contact-number">445168319</span>
    </li>
  </ul>

  <nav class="tab-bar">
    <div class="tab-settings">
      <svg width="40" height="40" viewBox="0 0 40 40" aria-label="Settings" role="img">
        <path fill="#fff" fill-rule="evenodd" d="M17 2h6l1 5 4 2 4-3 4 4-3 4 2 4 5 1v6l-5 1-2 4 3 4-4 4-4-3-4 2-1 5h-6l-1-5-4-2-4 3-4-4 3-4-2-4-5-1v-6l5-1 2-4-3-4 4-4 4 3 4-2z M20 13a7 7 0 1 0 0.01 0z"/>
      </svg>
    </div>
    <div class="tab-more" aria-label="More"><span></span><span></span><span></span></div>
  </nav>
</div>
</body>
</html>
```